Clark County Assessor Canditate

We need a billboard ad for a political candidate Tessa Harrow who is running for Clark County Assessor in an upcoming election. Needs to be simple and to the point to get the people to see the name "Tessa Harrow" and what to vote for "Clark County Assessor" in Las Vegas, NV. Also the billboard visibility is best in the top side of the sign, so the information should be most prominent in the top right, middle, left sides.The size of the billboard is 14 ft Height X 48 ft Wide Also needs some bright colors that are noticable from a freeway viewed billboard.Designers - I need to have "Paid for by Tessa Harrow for Clark County Assessor" on the sign
I have uploaded a few headshots you can work with to create a design. Thank you,

http://tessaharrow-vote.info/

Voters

Political

• Name, what I am voting for, and some image that represents Las Vegas and/or Nevada

```html
<!DOCTYPE html>
<html lang="en">
<head>
<meta charset="utf-8">
<title>Vote Tessa Harrow – Clark County Assessor</title>
<link rel="stylesheet" href="https://fonts.googleapis.com/css2?family=Rubik:wght@400;700;800&display=swap">
<style>
  :root {
    --navy: #044f95;
    --red: #e00000;
    --white: #ffffff;
    --page: #e9edf2;
    --portrait-light: #d9b98a;
    --portrait-dark: #2a2630;
    --seal-ring: #1f2f7a;
    --seal-gold: #c9a24a;
    --seal-sky: #a9c8e4;
  }
  * { margin: 0; padding: 0; box-sizing: border-box; }
  html, body {
    width: 1200px; height: 727px; overflow: hidden;
    background: var(--page);
  }
  .billboard {
    position: absolute; left: 0; top: 182px;
    width: 1200px; height: 363px;
    background: var(--white);
    overflow: hidden;
  }
  .portrait-panel {
    position: absolute; left: 0; top: 0;
    width: 417px; height: 363px;
    background: var(--navy);
  }
  .portrait {
    position: absolute; left: 42px; top: 11px;
    width: 340px; height: 352px;
    border-radius: 150px 150px 0 0;
    background: linear-gradient(180deg, var(--portrait-light) 0%, var(--portrait-light) 55%, var(--portrait-dark) 72%, var(--portrait-dark) 100%);
  }
  .vote {
    position: absolute; left: 456px; top: 18px;
    font-family: "Rubik", sans-serif;
    font-weight: 800;
    font-size: 72px; line-height: 1;
    color: var(--navy);
    letter-spacing: 1px;
  }
  .location-tab {
    position: absolute; left: 797px; top: 46px;
    width: 403px; height: 60px;
  }
  .location {
    position: absolute; right: 38px; top: 52px;
    font-family: "Rubik", sans-serif;
    font-weight: 700;
    font-size: 34px; line-height: 48px;
    color: var(--white);
  }
  .accent-bar {
    position: absolute; left: 417px; top: 106px;
    width: 39px; height: 173px;
    background: var(--red);
  }
  .seal {
    position: absolute; left: 471px; top: 111px;
    width: 158px; height: 158px;
  }
  .name-panel {
    position: absolute; left: 643px; top: 106px;
    width: 557px; height: 176px;
    background: var(--red);
    color: var(--white);
  }
  .candidate-name {
    position: absolute; left: 26px; top: 30px;
    max-width: 505px;
    font-family: "Rubik", sans-serif;
    font-weight: 700;
    font-size: 70px; line-height: 80px;
    white-space: nowrap;
  }
  .paid-for {
    position: absolute; left: 28px; top: 117px;
    font-family: "Rubik", sans-serif;
    font-weight: 400;
    font-size: 19px; letter-spacing: 0.4px;
    white-space: nowrap;
  }
  .paid-for strong { font-weight: 700; }
</style>
</head>
<body>
  <main class="billboard">
    <section class="portrait-panel">
      <div class="portrait" role="img" aria-label="Headshot photo of candidate Tessa Harrow"></div>
    </section>

    <h1 class="vote">VOTE</h1>

    <svg class="location-tab" viewBox="0 0 403 60" aria-hidden="true">
      <polygon points="40,0 403,0 403,60 0,60" fill="var(--navy)"/>
    </svg>
    <p class="location">In Las Vegas, NV</p>

    <div class="accent-bar"></div>

    <svg class="seal" viewBox="0 0 158 158" role="img" aria-label="State of Nevada seal emblem">
      <circle cx="79" cy="79" r="78" fill="var(--seal-ring)"/>
      <circle cx="79" cy="79" r="54" fill="var(--seal-gold)"/>
      <circle cx="79" cy="79" r="50" fill="var(--seal-sky)"/>
    </svg>

    <section class="name-panel">
      <h2 class="candidate-name">Tessa Harrow</h2>
      <p class="paid-for">Paid for by Tessa <strong>Harrow</strong> for Clark County Assessor</p>
    </section>
  </main>
</body>
</html>
```